Fernlow Accounting Business Card design

We need a stand out business card design for Accounting practice based in Australia specialising in pubs, clubs and hotels. We help venues maximise margins, create time and manage cashflow. One club we have been working with for the last 6 months has increased revenue by 3% and margin by 5% in this time frame. We have a back office outsourced system that costs less than having a full time employee and also allows the venues the added benefit of:<br/>-using the office space to become a revenue generating opportunity. <br/>-a complete system to enhance governance, accountability and efficiency within their operation<br/>-52 weeks cover so no hassle to cover annual/sick .. leave<br/><br/>We would like to see designs that use the colours of our logo (green & blue).
Target Market(s)
Australian Pubs, Clubs & Hotels abookkeeping, accounting and tax services
Industry/Entity Type
Accountant
Contact Information for Business Card
Miriam Colbeck CPA
Principal
Accountant Tax Agent
Miriam@FernlowAccounting.example.au
0418 369 514
www.fernlowaccounting.example.au
Accounting / Payroll / Tax / SMSF / Technology
Colors
Designer to choose colors to be used in the design.
Look and feel

```html
<!DOCTYPE html>
<html lang="en">
<head>
<meta charset="utf-8">
<title>Fernlow Accounting Business Card</title>
<link href="https://fonts.googleapis.com/css2?family=Nunito+Sans:wght@400;600;700&display=swap" rel="stylesheet">
<style>
  :root {
    --backdrop: #2a2c2f;
    --card: #1f1e2c;
    --blue: #2f5bc8;
    --green: #2b8c42;
    --ink: #e6e6ee;
    --ink-soft: #c9c9d4;
  }
  * { box-sizing: border-box; margin: 0; padding: 0; }
  html, body {
    width: 1200px; height: 900px; overflow: hidden;
    background: var(--backdrop);
    font-family: "Nunito Sans", Arial, sans-serif;
  }
  .canvas {
    width: 1200px; height: 900px;
    display: flex; flex-direction: column;
    align-items: center; justify-content: center; gap: 60px;
  }
  .card {
    width: 630px; height: 360px;
    background: var(--card);
    border-radius: 4px;
    box-shadow: 0 10px 30px rgba(0,0,0,.45);
    position: relative;
  }
  .brand {
    display: flex; align-items: center; gap: 12px;
  }
  .brand-dot {
    width: 22px; height: 22px; border-radius: 50%;
    background: var(--green); flex: none;
  }
  .brand-name {
    font-weight: 700; color: var(--blue);
    white-space: nowrap;
  }
  /* front */
  .card-front {
    display: flex; flex-direction: column;
    align-items: center; justify-content: center; gap: 18px;
  }
  .card-front .brand-name { font-size: 40px; }
  .card-front .brand-dot { width: 30px; height: 30px; }
  .services {
    color: var(--blue); font-size: 16px; letter-spacing: .5px;
  }
  /* back */
  .card-back {
    display: flex; align-items: center;
    padding: 0 48px;
  }
  .card-back .brand { width: 270px; }
  .card-back .brand-name { font-size: 26px; }
  .divider {
    width: 1.5px; height: 190px; background: var(--blue);
    margin: 0 34px 0 10px;
  }
  .details { color: var(--ink); }
  .person-name { font-size: 22px; font-weight: 600; }
  .person-role { font-size: 12px; color: var(--blue); margin-top: 4px; }
  .person-title { font-size: 14px; color: var(--ink-soft); margin-top: 4px; }
  .contact-list { list-style: none; margin-top: 18px; }
  .contact-list li {
    display: flex; align-items: center; gap: 10px;
    font-size: 13px; color: var(--ink-soft); margin-top: 7px;
  }
  .contact-list svg { width: 12px; height: 12px; fill: var(--blue); flex: none; }
</style>
</head>
<body>
<main class="canvas">
  <section class="card card-front" aria-label="Card front">
    <div class="brand">
      <span class="brand-dot"></span>
      <span class="brand-name">Fernlow Accounting</span>
    </div>
    <p class="services">Accounting / Payroll / Tax / SMSF / Technology</p>
  </section>

  <section class="card card-back" aria-label="Card back">
    <div class="brand">
      <span class="brand-dot"></span>
      <span class="brand-name">Fernlow Accounting</span>
    </div>
    <div class="divider"></div>
    <div class="details">
      <p class="person-name">Miriam Colbeck CPA</p>
      <p class="person-role">Principal</p>
      <p class="person-title">Accountant Tax Agent</p>
      <ul class="contact-list">
        <li>
          <svg viewBox="0 0 24 24" aria-hidden="true"><path d="M6.6 10.8a15.1 15.1 0 0 0 6.6 6.6l2.2-2.2a1 1 0 0 1 1-.25 11.4 11.4 0 0 0 3.6.57 1 1 0 0 1 1 1V20a1 1 0 0 1-1 1A17 17 0 0 1 3 4a1 1 0 0 1 1-1h3.5a1 1 0 0 1 1 1c0 1.25.2 2.45.57 3.57a1 1 0 0 1-.25 1z"/></svg>
          0418 369 514
        </li>
        <li>
          <svg viewBox="0 0 24 24" aria-hidden="true"><path d="M2 5h20v14H2z M2 5l10 8 10-8" /></svg>
          Miriam@FernlowAccounting.example.au
        </li>
        <li>
          <svg viewBox="0 0 24 24" aria-hidden="true"><circle cx="12" cy="12" r="10"/></svg>
          www.fernlowaccounting.example.au
        </li>
      </ul>
    </div>
  </section>
</main>
</body>
</html>
```